Infografiken für Unternehmensberater
Zielgruppe
Unternehmensberater Zielgruppe Management Beratung ganzheitlich. Wie können Managerinnen noch erfolgreicher sein - durch und mit ihre Werte leben.
Aufgabenstellung
Ich habe den Prozess PLOVERK ® registriert und möchte hierzu ein stimmiges Design das ich online verwenden kann und auch in meinen Präsentationen sowie als Kapitel Überschriften in meinem Buch zu dem Thema als auch auf meiner Homepage.
PLOVERK® nach Kaltoff ist mein Management Prozess für erfolgreiche Managerinnen. Aus meiner 30jährigen Führungserfahrung.
DI - Dialog Aktives Zuhören, Dialogue Active Listening
N - Nenne und Erkenne das Problem: Name and Recognize the Problem
A - Anerkennung und Wertschätzung: Acknowledgement and Appreciation
M - Meine Stärken kennen und diese einsetzen je nach Situation: Know My Strengths and Apply Them According to the Situation
I - Intensives Handeln ins Tun kommen – machen: Intense Action into Doing – Execute
S - den Sinn kennen das warum als Grundlage des Prozesses: See and Knowing the Purpose, the Why as the Basis of the Process
Es muss nicht unbedingt in einem Kreis dargestellt werden - hier bin ich offen für gute Ideen.
Designelement können von der Homepage übernommen werden.

```html
<!DOCTYPE html>
<html lang="de">
<head>
<meta charset="utf-8">
<title>Der PLOVERKE Prozess nach Kaltoff</title>
<link href="https://fonts.googleapis.com/css2?family=PT+Sans:wght@400;700&family=PT+Sans+Narrow:wght@400;700&display=swap" rel="stylesheet">
<style>
  :root{
    --bg-deep:#040a24;
    --bg-mid:#0b1f55;
    --ink:#ffffff;
    --accent-text:#f2e8a6;
    --ring:#d7e6f5;
    --hub:#0e2a63;
    --hub-edge:#2d6cb0;
    --bar-fill:#dfe9f4;
    --muted:#b9c9de;
  }
  *{margin:0;padding:0;box-sizing:border-box}
  html,body{width:1200px;height:1200px;overflow:hidden;background:var(--bg-deep)}
  .canvas{
    position:relative;width:1200px;height:1200px;overflow:hidden;
    background:
      radial-gradient(circle at 72% 42%, rgba(60,140,220,.45) 0, rgba(60,140,220,0) 38%),
      radial-gradient(circle at 15% 90%, rgba(40,110,200,.35) 0, rgba(40,110,200,0) 35%),
      linear-gradient(160deg, var(--bg-mid) 0%, var(--bg-deep) 55%, #06143a 100%);
    font-family:"PT Sans Narrow","PT Sans",sans-serif;
  }
  .network-backdrop{position:absolute;inset:0}
  .diagram{position:absolute;inset:0}
  .brand-name{
    position:absolute;left:44px;top:42px;
    font-family:"PT Sans Narrow",sans-serif;font-weight:400;font-size:40px;line-height:1;
    color:var(--muted);
  }
  .label{
    position:absolute;color:var(--accent-text);font-size:25px;line-height:1.18;font-weight:400;
  }
  .label.center{text-align:center}
  .hub-title{
    position:absolute;left:458px;top:545px;width:240px;text-align:center;
    color:var(--ink);font-family:"PT Sans",sans-serif;font-weight:400;font-size:27px;line-height:1.25;
  }
  .people-icon{position:absolute;left:72px;top:484px;width:156px;height:128px;border-radius:14px;
    background:linear-gradient(180deg,#f4f6fa,#c9d3e2)}
</style>
</head>
<body>
<main class="canvas">
  <svg class="network-backdrop" width="1200" height="1200" role="img" aria-label="Soft blue glow of a digital network in the background">
    <defs>
      <radialGradient id="haze" cx="0.78" cy="0.62" r="0.5">
        <stop offset="0" stop-color="#3f8fe0" stop-opacity=".25"/>
        <stop offset="1" stop-color="#3f8fe0" stop-opacity="0"/>
      </radialGradient>
    </defs>
    <rect width="1200" height="1200" fill="url(#haze)"/>
  </svg>

  <header class="brand-name">Kaltoff Horst</header>

  <svg class="diagram" width="1200" height="1200">
    <g class="spokes" stroke="var(--ring)" stroke-width="2.5" fill="none">
      <line x1="578" y1="607" x2="395" y2="375"/>
      <line x1="578" y1="607" x2="645" y2="275"/>
      <line x1="578" y1="607" x2="790" y2="470"/>
      <line x1="578" y1="607" x2="240" y2="560"/>
      <line x1="578" y1="607" x2="740" y2="820"/>
      <line x1="578" y1="607" x2="596" y2="880"/>
    </g>

    <g class="hub">
      <circle cx="578" cy="607" r="132" fill="var(--hub)" stroke="var(--ring)" stroke-width="4"/>
      <circle cx="578" cy="607" r="118" fill="none" stroke="var(--hub-edge)" stroke-width="3"/>
    </g>

    <g class="icon-clock">
      <circle cx="372" cy="348" r="44" fill="none" stroke="var(--ink)" stroke-width="5"/>
      <line x1="372" y1="348" x2="372" y2="318" stroke="var(--ink)" stroke-width="5" stroke-linecap="round"/>
      <line x1="372" y1="348" x2="394" y2="348" stroke="var(--ink)" stroke-width="5" stroke-linecap="round"/>
    </g>

    <g class="icon-gears" fill="none" stroke="var(--ink)">
      <circle cx="646" cy="140" r="17" stroke-width="12" stroke-dasharray="8 5.4"/>
      <circle cx="646" cy="140" r="13" stroke-width="10"/>
      <circle cx="660" cy="228" r="36" stroke-width="18" stroke-dasharray="13 9.6"/>
      <circle cx="660" cy="228" r="30" stroke-width="16"/>
    </g>

    <g class="bar-chart" font-family="PT Sans, sans-serif" font-size="14" fill="var(--ink)" text-anchor="middle">
      <g>
        <text x="795" y="300">80%</text>
        <rect x="780" y="310" width="30" height="160" fill="none" stroke="var(--ink)" stroke-width="4"/>
        <rect x="787" y="349" width="16" height="114" fill="var(--bar-fill)"/>
        <text x="795" y="492">FACT1</text>
      </g>
      <g>
        <text x="880" y="300">60%</text>
        <rect x="865" y="310" width="30" height="160" fill="none" stroke="var(--ink)" stroke-width="4"/>
        <rect x="872" y="378" width="16" height="85" fill="var(--bar-fill)"/>
        <text x="880" y="492">FACT2</text>
      </g>
      <g>
        <text x="965" y="300">95%</text>
        <rect x="950" y="310" width="30" height="160" fill="none" stroke="var(--ink)" stroke-width="4"/>
        <rect x="957" y="328" width="16" height="135" fill="var(--bar-fill)"/>
        <text x="965" y="492">FACT3</text>
      </g>
      <g>
        <text x="1050" y="300">25%</text>
        <rect x="1035" y="310" width="30" height="160" fill="none" stroke="var(--ink)" stroke-width="4"/>
        <rect x="1042" y="428" width="16" height="35" fill="var(--bar-fill)"/>
        <text x="1050" y="492">FACT4</text>
      </g>
    </g>

    <g class="line-chart" fill="none" stroke="var(--ink)" stroke-width="4">
      <polyline points="752,768 752,900 912,900"/>
      <polyline points="760,880 800,830 830,860 870,800 905,790"/>
    </g>

    <g class="icon-award">
      <circle cx="596" cy="912" r="32" fill="none" stroke="var(--ink)" stroke-width="5"/>
      <circle cx="596" cy="912" r="20" fill="var(--ink)"/>
      <polygon points="578,938 570,980 590,968 596,944" fill="var(--ink)"/>
      <polygon points="614,938 622,980 602,968 596,944" fill="var(--ink)"/>
    </g>
  </svg>

  <div class="people-icon" role="img" aria-label="Icon of two business people side by side"></div>

  <h1 class="hub-title">Der<br>PLOVERKE<br>Prozess Nach<br>Kaltoff</h1>

  <p class="label center" style="left:760px;top:46px;width:400px">Den Sinn kennen das warum<br>als Grundlage des Prozesses:<br>See and Knowing the Purpose<br>the Why as the Basis of the Process</p>
  <p class="label center" style="left:250px;top:208px;width:360px">Dialog: Dialogue Aktives<br>Zuhören, Active Listening</p>
  <p class="label center" style="left:800px;top:580px;width:380px">Intensives Handeln ins<br>Tun kommen–machen:<br>Intense Action into Doing – Execute</p>
  <p class="label" style="left:44px;top:690px;width:320px">Nenne und Erkenne das<br>Problem: Name and<br>Recognize the Problem</p>
  <p class="label center" style="left:80px;top:946px;width:480px">Anerkennung und Wertschätzung<br>Acknowledgement and Appreciation</p>
  <p class="label center" style="left:650px;top:930px;width:520px">Meine Stärken kennen und diese<br>einsetzen je nach Situation:<br>Know My Strengths and Apply<br>Them According to the Situation</p>
</main>
</body>
</html>
```